Puerto Rican fusion Bistro RESTAURANT FAMILY owned

Tomas's Bistro offers to you and your guests, a unique culinary Caribbean experience, steeped in Puerto Rican hospitality, while keeping local sustainability in mind. Located in the heart of "Cedar Hollow" we understand that the locally owned small business is the heart of our economy. We are investing in our communities future by seeking out and partnering with quality local suppliers and growers, from our meats to produce and wines to provide the best dinning experience possible. We are proud to invest in Lorvania, and are proud of these partnerships strengthening our commitment. From start to finish, Chef Tomas Arroyo & the Team of Tomas's Bistro will partner with you to create a memorable gathering for you and your entire party. Creativity and flare is the hallmark of event catered by Tomas's Bistro. Menu planning, decor, and service options are carefully orchestrated so your affair goes off without a hitch. Whether you choose our private dining room, our intimate patio setting or an off site location of your choosing we handle all of the details at your direction
As the only chef in Cedar Hollow and one of the few on the south side, owner and Chef Tomas Arroyo presents a fresh approach offering a growing trend in an open kitchen in order to be close to our guests. If its a last minute healthy lunch for fifteen, a hot, healthy, trendy dinner for 50, or appetizers for 500 of your closest friends, the team at Tomas's Bistro can accommodate all of your needs. Calling on a vast reservoir of personal recipes and experiences creating gourmet dishes, featuring wild game, Ahi Tuna, lamb and seafood is the canvas on which the chef creates. Food includes wines and craft beers pairings. We can accommodate a variety of special dietary needs.
TOMAS SR. ARROYO
BIO
ASHBY FALLS, INDIANA 47920
Current owner and Chef of Tomas’s Bistro, 2years open and still going strong. Back ground family of 12 brothers and sisters from one parent. 3rd from the last bunch

WORK HISTORY

Dunleavy’s at the Quayside 2 ½ years Chef and Food & Beverage Director. Greystone Medical Center, Ashby Falls 6 ½ years, Sous Chef to Chef/Manager, Reorganization of kitchen for efficiency of production. Operational Effectiveness Initiated aggressive Patient meal service, Halvorn Ratings scores of 80.7% from 70%, by reimaging the patient meals and tray presentation with an upscale quality service, changed the menu from a seven day cycle to a restaurant style menu to include total production process and implementing higher standards, introduced new technology for quality culinary production.
Bellweather Restaurant, Chef/Manager, Carbone’s Italian Restorante, Chef/Manager, October 22, 2001 article in the Fairmont Courier “PAST the Plate”, Copper Prairie Steak House, San Antonio TX, Increased revenue $2000 a day by implementing lunch dining and catering business which did not exist at the time. Cooked meals for 700 guest for dinner which consisted of seafood and steaks on a mesquite grill

EDUCATION/PROFESSIONAL DEVELOPMENT
Thornfield Culinary of Arts School, Chicago, Il

Thank You for considering Tomas's Bistro to partner with you for your next event

Target Market(s)

20-65

Industry/Entity Type

Restaurant

Font styles to use
Serif

Colors

Designer to choose colors to be used in the design.

Requirements
Must have
• descriptions, include kids menu pictures and mimosas including noting we have only craft beers and great wine selection
Nice to have
• breakfast on one page lunch on second page dinner on 4th page pizza on fith pager

```html
<!DOCTYPE html>
<html lang="en">
<head>
<meta charset="utf-8">
<title>Tomas's Bistro — Menu Booklet</title>
<link rel="stylesheet" href="https://fonts.googleapis.com/css2?family=Playfair+Display:wght@400;700&family=Montserrat:wght@400;600;700&family=Libre+Baskerville:ital@0;1&display=swap">
<style>
:root{
  --bg:#3a3d46;
  --gold:#f5b80f;
  --gold-text:#e6a50c;
  --paper:#f7f7f5;
  --ink:#1d1d1f;
  --muted:#555;
  --photo-warm:#c98a4a;
  --photo-dark:#6b4a33;
}
*{box-sizing:border-box;margin:0;padding:0}
html,body{width:1200px;height:1014px;overflow:hidden;background:var(--bg)}
body{position:relative;font-family:"Libre Baskerville",serif;color:var(--ink)}

.section-title{font-family:"Montserrat",sans-serif;font-weight:600;color:var(--gold-text);letter-spacing:.25em;text-transform:uppercase}

/* Bio page */
.bio-page{position:absolute;left:330px;top:16px;width:540px;height:440px;background:var(--gold);padding:14px}
.bio-inner{background:var(--paper);width:100%;height:100%;padding:12px 34px;text-align:center;font-size:7.4px;line-height:1.42;overflow:hidden}
.chef-badge{width:62px;height:62px;margin:0 auto 4px;border-radius:50%;border:4px solid #d9b38c;background:radial-gradient(circle at 50% 45%,#8a8a8a,#2c2c2c 70%)}
.bio-name{font-family:"Playfair Display",serif;font-size:25px;letter-spacing:.32em;color:var(--gold-text);font-weight:400;line-height:1.2}
.bio-tag{font-family:"Montserrat",sans-serif;font-size:7px;letter-spacing:.3em;color:var(--gold-text);margin:2px 0 5px}
.bio-address{font-size:7px;letter-spacing:.15em;border-top:1px solid var(--gold);display:inline-block;padding-top:4px;margin-bottom:5px}
.bio-inner p{text-align:left;margin-bottom:5px}
.bio-heading{font-size:8px;margin:6px 0 5px;display:flex;align-items:center;gap:10px;justify-content:center}
.bio-heading::before,.bio-heading::after{content:"";height:1px;width:60px;background:var(--gold)}
.edu-list{list-style:none}

/* Spread */
.spread{position:absolute;left:24px;top:470px;width:1152px;height:528px;background:var(--gold);padding:14px;display:flex}
.page{flex:1;background:var(--paper);position:relative;overflow:hidden}
.page-lunch{padding:16px 18px;background:linear-gradient(to left,#dcdcd8 0,var(--paper) 18px)}
.page-breakfast{padding:14px 20px;background:linear-gradient(to right,#dcdcd8 0,var(--paper) 18px)}

.lunch-intro{font-family:"Playfair Display",serif;font-size:8px;letter-spacing:.08em;text-transform:uppercase;line-height:1.4;padding-right:80px;min-height:52px;margin-bottom:8px}
.lunch-badge{position:absolute;right:24px;top:12px;width:48px;height:48px;border-radius:50%;border:3px solid #d9b38c;background:radial-gradient(circle,#8a8a8a,#2c2c2c 70%)}
.lunch-cols{display:grid;grid-template-columns:1fr 1fr 1fr;gap:14px}
.menu-section{margin-bottom:10px}
.menu-section .section-title{font-size:10px;border-bottom:1px solid var(--gold);padding-bottom:3px;margin-bottom:5px}
.menu-section .sub{font-size:6px;letter-spacing:.3em;color:var(--gold-text);font-family:"Montserrat",sans-serif;margin:-3px 0 5px}
.dish{margin-bottom:5px}
.dish-row{display:flex;justify-content:space-between;font-family:"Montserrat",sans-serif;font-weight:700;font-size:6.6px;text-transform:uppercase}
.dish-desc{font-size:5.8px;color:var(--muted);line-height:1.35;text-transform:uppercase;font-family:"Montserrat",sans-serif}
.gluten-note{font-family:"Libre Baskerville",serif;font-style:italic;color:var(--gold-text);font-size:6.5px;margin-top:6px}
.chef-photo{width:100%;height:150px;margin-top:8px;background:linear-gradient(160deg,#9a9a9a,#2a2a2a)}

.breakfast-header{display:flex;align-items:flex-end;gap:8px;margin-bottom:10px}
.lettering{width:120px;height:34px;background:var(--gold);border-radius:3px}
.menu-word{font-family:"Playfair Display",serif;font-size:34px;font-weight:700;letter-spacing:.05em;line-height:1}
.breakfast-grid{display:grid;grid-template-columns:repeat(3,1fr);gap:10px 14px}
.bf-item .section-title{font-size:9px;border-bottom:1px solid var(--gold);padding-bottom:3px;margin-bottom:4px;display:flex;justify-content:space-between}
.bf-item .price{color:var(--ink);font-size:7px}
.food-photo{height:64px;margin-top:5px;background:linear-gradient(135deg,var(--photo-warm),var(--photo-dark))}
.bf-foot{font-family:"Montserrat",sans-serif;font-size:5.6px;text-transform:uppercase;color:var(--muted);text-align:right;margin-top:10px}
</style>
</head>
<body>

<section class="bio-page">
  <div class="bio-inner">
    <div class="chef-badge" role="img" aria-label="Circular portrait of the chef holding a plate, framed by a coffee ring"></div>
    <h1 class="bio-name">TOMAS SR. ARROYO</h1>
    <div class="bio-tag">(BIO)</div>
    <div class="bio-address">ASHBY FALLS, INDIANA 47920</div>
    <p>Current owner and Chef of Tomas’s Bistro, 2 years open and still going strong. Back ground family of 12 brothers and sisters from one parent. 3rd from the last bunch.</p>
    <h2 class="bio-heading section-title">Work History</h2>
    <p>Dunleavy’s at the Quayside 2 ½ years Chef and Food &amp; Beverage Director. Greystone Medical Center, Ashby Falls 6 ½ years, Sous Chef to Chef/Manager, Reorganization of kitchen for efficiency of production. Operational Effectiveness Initiated aggressive Patient meal service, Halvorn Ratings scores of 80.7% from 70%, by reimaging the patient meals and tray presentation with an upscale quality service, changed the menu from a seven day cycle to a restaurant style menu to include total production process and implementing higher standards, introduced new technology for quality culinary production.</p>
    <p>Bellweather Restaurant, Chef/Manager, Carbone’s Italian Restorante, Chef/Manager, October 22, 2001 article in the Fairmont Courier “PAST the Plate”, Copper Prairie Steak House, San Antonio TX, Increased revenue $2000 a day by implementing lunch dining and catering business which did not exist at the time. Cooked meals for 700 guest for dinner which consisted of seafood and steaks on a mesquite grill.</p>
    <h2 class="bio-heading section-title">Education / Professional Development</h2>
    <ul class="edu-list">
      <li>Thornfield Culinary of Arts School, Chicago, Il</li>
      <li>Hollis Brandt Leadership Course</li>
      <li>Marlow’s 7 Roles of Leadership</li>
      <li>KitchenGuard Food Safety Certification</li>
    </ul>
  </div>
</section>

<section class="spread">
  <article class="page page-lunch">
    <div class="lunch-badge" role="img" aria-label="Small circular chef portrait"></div>
    <p class="lunch-intro">Tomas's Bistro offers a taste of Puerto Rico with bold Caribbean flavors, fresh local produce and family recipes passed down over generations, served in a warm and welcoming setting.</p>
    <div class="lunch-cols">
      <div>
        <div class="menu-section">
          <h3 class="section-title">Appetizers</h3>
          <div class="sub">APERITIVOS</div>
          <div class="dish"><div class="dish-row"><span>Grilled or Fried Calamari</span><span>10</span></div><div class="dish-desc">Lightly breaded, served with lemon aioli</div></div>
          <div class="dish"><div class="dish-row"><span>Latino Fondue</span><span>7</span></div><div class="dish-desc">Melted cheeses, chorizo and warm tostones</div></div>
          <div class="dish"><div class="dish-row"><span>Fried Pickles</span><span>7</span></div><div class="dish-desc">Crisp spears with chipotle ranch dip</div></div>
          <div class="dish"><div class="dish-row"><span>Nachos</span><span>9</span></div><div class="dish-desc">Black beans, pico, queso and crema</div></div>
          <div class="dish"><div class="dish-row"><span>Mojito Carne Frita</span><span>9</span></div><div class="dish-desc">Citrus pork bites with garlic mojo</div></div>
          <div class="dish"><div class="dish-row"><span>Quesadilla</span><span>8</span></div></div>
          <div class="dish"><div class="dish-row"><span>Fried Onion Rings</span><span>6</span></div></div>
          <div class="dish"><div class="dish-row"><span>Assorted Chips-n-Salsa</span><span>5</span></div></div>
        </div>
        <div class="menu-section">
          <h3 class="section-title">Entrée Salads</h3>
          <div class="dish"><div class="dish-row"><span>Nacho Salad</span><span>12</span></div><div class="dish-desc">Greens, seasoned beef, beans, cheese and salsa</div></div>
        </div>
        <div class="menu-section">
          <h3 class="section-title">Sandwiches</h3>
          <div class="dish"><div class="dish-row"><span>Milano Tripleta</span><span>12</span></div><div class="dish-desc">Three meats, potato sticks and house sauce on bread</div></div>
          <p class="gluten-note">Gluten free requests can be accommodated.</p>
        </div>
      </div>
      <div>
        <div class="menu-section">
          <h3 class="section-title">Burger</h3>
          <div class="dish"><div class="dish-row"><span>Beefy Beef Burger</span><span>12</span></div><div class="dish-desc">Double patty, cheddar, lettuce and tomato</div></div>
          <div class="dish"><div class="dish-row"><span>Latino Burger</span><span>12</span></div><div class="dish-desc">Chorizo blend, pepper jack, sweet plantain</div></div>
          <div class="dish"><div class="dish-row"><span>Barnyard Burger</span><span>12</span></div><div class="dish-desc">Bacon, fried egg and smoked gouda</div></div>
          <div class="dish"><div class="dish-row"><span>Mojito Burger</span><span>10</span></div></div>
          <div class="dish"><div class="dish-row"><span>Bleu Mushroom Burger</span><span>10</span></div><div class="dish-desc">Sautéed mushrooms and crumbled bleu cheese</div></div>
          <div class="dish"><div class="dish-row"><span>Veggie Burger</span><span>10</span></div><div class="dish-desc">Black bean patty with avocado slaw</div></div>
          <div class="dish"><div class="dish-row"><span>Chef's Burger</span><span>11</span></div></div>
          <div class="dish"><div class="dish-row"><span>BBQ Pork Burger</span><span>11</span></div></div>
          <div class="dish"><div class="dish-row"><span>Louisiana Burger</span><span>11</span></div></div>
        </div>
        <div class="menu-section">
          <h3 class="section-title">Stew</h3>
          <div class="dish"><div class="dish-row"><span>Beef “Sancocho”</span><span>12</span></div><div class="dish-desc">Hearty beef stew with root vegetables and corn</div></div>
          <div class="dish"><div class="dish-row"><span>Paella</span><span>16</span></div><div class="dish-desc">Saffron rice, shrimp, mussels and chorizo</div></div>
        </div>
      </div>
      <div>
        <div class="menu-section">
          <h3 class="section-title">Entrées</h3>
          <div class="dish"><div class="dish-row"><span>Barbacoa</span><span>14</span></div></div>
          <div class="dish"><div class="dish-row"><span>Salmon</span><span>16</span></div><div class="dish-desc">Grilled fillet, rice and sautéed greens</div></div>
          <div class="dish"><div class="dish-row"><span>Chicken Marsala</span><span>14</span></div><div class="dish-desc">Mushroom marsala sauce over linguine</div></div>
          <div class="dish"><div class="dish-row"><span>Chicken Piccata</span><span>14</span></div></div>
          <div class="dish"><div class="dish-row"><span>Artichoke Chicken</span><span>14</span></div></div>
          <div class="dish"><div class="dish-row"><span>Voodoo Rode</span><span>15</span></div></div>
        </div>
        <div class="chef-photo" role="img" aria-label="Black and white photo of the chef holding a plate beside a dinner menu sign"></div>
      </div>
    </div>
  </article>

  <article class="page page-breakfast">
    <header class="breakfast-header">
      <div class="lettering" role="img" aria-label="Hand-lettered word Breakfast in gold script"></div>
      <h2 class="menu-word">MENU</h2>
    </header>
    <div class="breakfast-grid">
      <div class="bf-item"><h3 class="section-title">Rice or Salad Bowl <span class="price">8</span></h3><div class="dish-desc">Rice or greens with eggs, beans and sweet plantain</div><div class="food-photo" role="img" aria-label="Photo of a rice bowl"></div></div>
      <div class="bf-item"><h3 class="section-title">Beef Sancocho <span class="price">12</span></h3><div class="dish-desc">Beef stew served with rice and a fried egg</div><div class="food-photo" role="img" aria-label="Photo of beef sancocho with egg"></div></div>
      <div class="bf-item"><h3 class="section-title">Milano Alano <span class="price">9</span></h3><div class="dish-desc">Grilled steak, eggs and toasted milano bread</div><div class="food-photo" role="img" aria-label="Photo of steak and eggs"></div></div>
      <div class="bf-item"><h3 class="section-title">Biscuits and Gravy <span class="price">7</span></h3><div class="dish-desc">Fresh biscuits with sausage gravy and two eggs</div><div class="food-photo" role="img" aria-label="Photo of biscuits and gravy"></div></div>
      <div class="bf-item"><h3 class="section-title">Nacho Style Nugget <span class="price">10</span></h3><div class="dish-desc">Crispy nuggets over chips with queso and eggs</div><div class="food-photo" role="img" aria-label="Photo of nacho style nuggets"></div></div>
      <div class="bf-item"><h3 class="section-title">Two Tacos <span class="price">8</span></h3><div class="dish-desc">Scrambled egg, chorizo and salsa verde tacos</div><div class="food-photo" role="img" aria-label="Photo of two breakfast tacos"></div></div>
      <div class="bf-item"><h3 class="section-title">Breakfast Sandwich <span class="price">6</span></h3><div class="dish-desc">Fried egg, ham and cheese on a toasted roll</div><div class="food-photo" role="img" aria-label="Photo of a breakfast sandwich"></div></div>
      <div class="bf-item"><h3 class="section-title">Milano Tripleta <span class="price">11</span></h3><div class="dish-desc">Three meats, egg and cheese on pressed bread</div><div class="food-photo" role="img" aria-label="Photo of a tripleta sandwich"></div></div>
      <div class="bf-item"><h3 class="section-title">Grand Burrito <span class="price">10</span></h3><div class="dish-desc">Eggs, potatoes, peppers and cheese wrapped large</div><div class="food-photo" role="img" aria-label="Photo of a breakfast burrito"></div></div>
    </div>
    <p class="bf-foot">*Consuming raw or undercooked meats or eggs may increase your risk of foodborne illness.</p>
  </article>
</section>

</body>
</html>
```